Customizable Form Generation Website

This will be a place for users to quickly generate numerous forms from a categorized list. As the forms are templates with field variables, the site must be able to substitute ‘real data’ for template variable data. This tool will allow for quick custom forms on-demand.

The landing page is attached. We need the User Experience and User Interface solved for us.

EXAMPLE:
——————————————————————-
Dear {{PatientFirstName}},

Please come back for an examination on {{SelectedDate}} with Doctor {{SelectedProvider}}.

Sincerely,

{{SelectedAuthor}}
——————————————————————-

Coming to the Forms Landing Page, the user will see the forms available to select. The user will then click to select a form.

At some point, the user must resolve the variables in the form. For instance, there are the following variables in the above example: PatientFirstName, SelectedDate, SelectedProvider, and SelectedAuthor. We must give the user a chance to select the values for these variables. Using a dropdown combobox will probably work for most. Getting a date selector will be required if the variable happens to contain the string 'date'.

Is it best to preselect common variables before opening the form, or is it best to dynamically scan the template, then give the user the option to give values to each variable found?

The design must include a way for users to upload additional forms. Forms will most probably be PDF, .DOC, .TXT files. This allows users to develop simple or fancy forms of their choosing., then simply drop them into the site for future use.

The design must include a way for users to create new forms. The form creation tool must present to the user the list of predefined variables like {{PatientLastName}} for easy insertion into the form writer. Anytime "{{}}" are used, developers will recognize that as a variable that needs to be resolved.

The forms will be separated into categories as follows:

OFFICE:
- Letterhead
- Sign-In Sheet
- Fax Cover Sheet
SCHEDULER:
- Appointment Reminder
- Missed Appointment Policy
PATIENT:
- Intake Form
- Patient Discharge
- Return to Work or School
- Excuse Slip
- Consent to Treat a Minor
- Verify Non-Pregnancy
RELEASE:
- Health Information Release Form
- X-Ray Release Form
CERTIFICATES:
- Certificate of Care
- Disability Certificate
INSURANCE:
- Authorization to Bill Insurance
- Assignment Authorization
OTHER:
- Free Massage
- Free Vitamins

The design must include a way to add/customize categories. Categories are for organizing the forms logically.

We welcome ANY questions to help understand the requirements.

Good luck!

Industry/Entity Type

Healthcare

Number of Pages Required

3 page

Requirements
Must have
• Must Follow VELLUM PATTERN standards
Nice to have
• Great User Experience. Simple, Fast, Clever.
Should not have
• nothing to add here

```html
<!DOCTYPE html>
<html lang="en">
<head>
<meta charset="utf-8">
<title>FormNest – Category</title>
<link href="https://fonts.googleapis.com/css2?family=Rubik:wght@400;500&display=swap" rel="stylesheet">
<style>
  :root {
    --navy: #0c1b2e;
    --navy-deep: #0f2140;
    --brand-blue: #1c5a92;
    --ink: #1c2b3a;
    --muted: #5b6672;
    --surface: #f4f4f4;
    --line: #e2e2e2;
    --field-line: #d6d6d6;
    --white: #ffffff;
  }
  * { box-sizing: border-box; margin: 0; padding: 0; }
  html, body { width: 1200px; height: 606px; overflow: hidden; }
  body { position: relative; background: var(--white); font-family: "Rubik", sans-serif; color: var(--ink); }

  .topbar { position: absolute; left: 0; top: 0; width: 1200px; height: 42px; background: var(--navy); color: var(--white); }
  .brand { position: absolute; left: 50px; top: 12px; font-size: 14px; font-weight: 500; letter-spacing: .1px; }
  .topnav { position: absolute; right: 49px; top: 15px; display: flex; gap: 20px; font-size: 9.5px; font-weight: 500; }

  .page-title { position: absolute; left: 196px; top: 69px; font-size: 19px; font-weight: 400; }
  .btn-create { position: absolute; left: 866px; top: 64px; width: 138px; height: 35px; background: var(--brand-blue); color: var(--white); border: 0; font: 500 10px "Rubik", sans-serif; }

  .categories { position: absolute; left: 196px; top: 121px; width: 208px; height: 394px; background: var(--surface); }
  .cat { position: absolute; left: 0; width: 206px; border-top: 1px solid var(--line); }
  .cat-head { position: absolute; left: 18px; font-size: 12.5px; font-weight: 500; }
  .cat-toggle { position: absolute; right: 16px; font-size: 12px; font-weight: 500; }
  .cat.open .accent { position: absolute; left: 0; top: 15px; width: 2px; height: 18px; background: var(--brand-blue); }
  .form-list { position: absolute; left: 18px; top: 44px; list-style: none; font-size: 9.5px; line-height: 20px; }
  .form-list .active { text-decoration: underline; }

  .btn-upload { position: absolute; left: 196px; top: 525px; width: 206px; height: 35px; background: var(--white); border: 1px solid var(--navy); font: 500 9.5px "Rubik", sans-serif; color: var(--ink); }

  .form-panel { position: absolute; left: 421px; top: 121px; width: 583px; height: 439px; border: 1px solid var(--line); }
  .form-header { position: absolute; left: 0; top: 0; width: 581px; height: 98px; border-bottom: 1px solid var(--line); }
  .logo-box { position: absolute; left: 17px; top: 17px; width: 63px; height: 63px; background: var(--navy-deep); color: var(--white); font-size: 15px; display: flex; align-items: center; justify-content: center; }
  .company { position: absolute; left: 90px; top: 39px; font-size: 15px; }

  .form-title { position: absolute; left: 17px; top: 119px; font-size: 20px; font-weight: 400; }
  .label { position: absolute; font-size: 10.5px; }
  .field { position: absolute; width: 265px; height: 35px; background: var(--surface); border: 1px solid var(--field-line); font-size: 9.5px; color: var(--muted); display: flex; align-items: center; padding-left: 8px; gap: 6px; }
  .field .caret { position: absolute; right: 12px; top: 14px; }

  .link-btn { position: absolute; font-size: 10px; font-weight: 500; }
  .btn-download { position: absolute; left: 491px; top: 382px; width: 74px; height: 35px; background: var(--navy-deep); color: var(--white); border: 0; font: 500 10px "Rubik", sans-serif; }
</style>
</head>
<body>
  <header class="topbar">
    <div class="brand">FormNest</div>
    <nav class="topnav"><span>Sample healthcare practice</span><span>Welcome back test</span><span>Log out</span></nav>
  </header>

  <h1 class="page-title">Category</h1>
  <button class="btn-create">Create custom form</button>

  <aside class="categories">
    <div class="cat open" style="top:0;height:112px;border-top:0">
      <span class="accent"></span>
      <span class="cat-head" style="top:16px">Office</span>
      <span class="cat-toggle" style="top:15px">–</span>
      <ul class="form-list">
        <li class="active">Letterhead</li>
        <li>Sign-In Sheet</li>
        <li>Fax Cover Sheet</li>
      </ul>
    </div>
    <div class="cat" style="top:112px;height:47px"><span class="cat-head" style="top:15px">Scheduler</span><span class="cat-toggle" style="top:15px">+</span></div>
    <div class="cat" style="top:159px;height:47px"><span class="cat-head" style="top:15px">Patient</span><span class="cat-toggle" style="top:15px">+</span></div>
    <div class="cat" style="top:206px;height:47px"><span class="cat-head" style="top:15px">Release</span><span class="cat-toggle" style="top:15px">+</span></div>
    <div class="cat" style="top:253px;height:47px"><span class="cat-head" style="top:15px">Certificates</span><span class="cat-toggle" style="top:15px">+</span></div>
    <div class="cat" style="top:300px;height:47px"><span class="cat-head" style="top:15px">Insurance</span><span class="cat-toggle" style="top:15px">+</span></div>
    <div class="cat" style="top:347px;height:47px"><span class="cat-head" style="top:15px">Other</span><span class="cat-toggle" style="top:15px">+</span></div>
  </aside>
  <button class="btn-upload">Upload additional forms</button>

  <main class="form-panel">
    <div class="form-header">
      <div class="logo-box">Logo</div>
      <div class="company">Company name</div>
    </div>

    <h2 class="form-title">Patient Form</h2>

    <span class="label" style="left:17px;top:161px">Dear</span>
    <div class="field" style="left:17px;top:180px">Patient First Name</div>
    <div class="field" style="left:299px;top:180px">Patient Last Name</div>

    <span class="label" style="left:17px;top:235px">Please come back for an examination on</span>
    <span class="label" style="left:299px;top:235px">With Doctor</span>
    <div class="field" style="left:17px;top:253px">
      <svg width="13" height="13" viewBox="0 0 13 13" fill="none" stroke="#5b6672" stroke-width="1"><rect x="1" y="2" width="11" height="10" rx="1"/><line x1="1" y1="5" x2="12" y2="5"/><line x1="4" y1="0.5" x2="4" y2="3"/><line x1="9" y1="0.5" x2="9" y2="3"/></svg>
      SelectedDate
      <svg class="caret" width="7" height="5" viewBox="0 0 7 5"><path d="M0 0h7L3.5 5z" fill="#3a4550"/></svg>
    </div>
    <div class="field" style="left:299px;top:253px">
      <svg width="13" height="13" viewBox="0 0 13 13" fill="none" stroke="#5b6672" stroke-width="1"><circle cx="6.5" cy="4" r="2.8"/><path d="M1.5 12.5c0-3 2.2-4.7 5-4.7s5 1.7 5 4.7z"/></svg>
      SelectedProvider
      <svg class="caret" width="7" height="5" viewBox="0 0 7 5"><path d="M0 0h7L3.5 5z" fill="#3a4550"/></svg>
    </div>

    <span class="label" style="left:17px;top:309px">Sincerely,</span>
    <div class="field" style="left:17px;top:327px">
      SelectedAuthor
      <svg class="caret" width="7" height="5" viewBox="0 0 7 5"><path d="M0 0h7L3.5 5z" fill="#3a4550"/></svg>
    </div>

    <span class="link-btn" style="left:17px;top:393px">Save</span>
    <span class="link-btn" style="left:443px;top:393px">Preview</span>
    <button class="btn-download">Download</button>
  </main>
</body>
</html>
```